New UK IT business
Business cards etc
Project: New UK IT business
New UK IT business - Environment
Creative Brief
Bright & Fun-filled
Cobalt Harvest Limited or Ltd - Gordon Pressey
Director
14 Brindle Lane Oakhurst Trading Park Fenwick Cross Herts HP9 3QL United Kingdom
gord@cobaltharvest-example.com
www.cobaltharvest-example.com
please do one card for Gord Pressey - Director and one for Rosalind Pressey - Director and one for Company - with no name
full colour - simple logo and website address only for the inside of the card i want it to have the fold on the horizontal meaning 55mm down the front with logo and name and address details the back as described above the inside I would like a picture of business people and have the messages of Redundant IT and Computer equipment Business people - corporate business people wanted All UK areas please suggest what you think and design around it thanks I will be available to answer questions when i see some designs for inspiration

```html
<!DOCTYPE html>
<html lang="en">
<head>
<meta charset="utf-8">
<title>Cobalt Harvest Limited – Stationery Set</title>
<link rel="stylesheet" href="https://fonts.googleapis.com/css2?family=Open+Sans:wght@400;700&display=swap">
<style>
  :root {
    --stage: #3a332d;
    --paper: #ffffff;
    --paper-shade: #eef0ee;
    --green-dark: #0f3d12;
    --green: #1f6e22;
    --green-light: #4aa23f;
    --grey-line: #c9cdc9;
    --ink: #3b3b3b;
    --label: #e6e1da;
  }
  * { box-sizing: border-box; margin: 0; padding: 0; }
  html, body { width: 1200px; height: 494px; overflow: hidden; }
  body {
    background: var(--stage);
    font-family: "Open Sans", Arial, sans-serif;
    color: var(--ink);
    position: relative;
  }
  .item { position: absolute; }
  .label {
    position: absolute;
    font-size: 6px;
    color: var(--label);
    letter-spacing: .2px;
    white-space: nowrap;
  }
  .sheet {
    position: absolute;
    background: var(--paper);
    box-shadow: 0 2px 6px rgba(0,0,0,.45);
    overflow: hidden;
  }
  .swoosh { position: absolute; left: 0; width: 100%; display: block; }
  .swoosh.top { top: 0; }
  .swoosh.bottom { bottom: 0; }
  .brand {
    position: absolute;
    display: flex;
    align-items: center;
    gap: 3px;
    font-weight: 700;
    color: var(--green);
    white-space: nowrap;
    text-transform: uppercase;
    z-index: 1;
  }
  .brand .dot { border-radius: 50%; background: var(--green); flex: none; }
  .brand.on-dark { color: var(--paper); }
  .brand.on-dark .dot { background: var(--paper); }
  .small-text { position: absolute; font-size: 3.4px; line-height: 1.35; color: var(--ink); white-space: nowrap; }
  .lines { position: absolute; }
  .lines i { display: block; height: 1.5px; background: var(--grey-line); margin-bottom: 3px; }

  .invoice-table { position: absolute; left: 12px; right: 12px; top: 98px; border-collapse: collapse; font-size: 3.4px; }
  .invoice-table th { background: var(--green); color: var(--paper); text-align: left; padding: 1.5px 2px; font-weight: 700; }
  .invoice-table td { border-bottom: .6px solid var(--grey-line); padding: 2.5px 2px; }
  .invoice-title { position: absolute; right: 12px; top: 62px; font-size: 8px; font-weight: 700; color: var(--green); }

  .folder-panel { position: absolute; top: 0; height: 100%; background: var(--paper); overflow: hidden; box-shadow: 0 2px 6px rgba(0,0,0,.45); }
  .folder-front { background: linear-gradient(160deg, var(--green-light) 0%, var(--green) 40%, var(--green-dark) 100%); }
  .folder-front .ring { position: absolute; left: 50%; top: 42%; width: 46px; height: 46px; margin: -23px 0 0 -23px; border-radius: 50%; background: radial-gradient(circle, rgba(255,255,255,.25), rgba(255,255,255,0) 70%); }
  .pocket { position: absolute; left: 0; right: 0; bottom: 0; height: 42%; }
  .card-slot { position: absolute; left: 40%; top: 56%; width: 44px; height: 26px; border: .8px solid var(--grey-line); border-radius: 2px; background: var(--paper); }

  .card { position: absolute; width: 86px; height: 50px; background: var(--paper); box-shadow: 0 1px 4px rgba(0,0,0,.5); overflow: hidden; }
  .card.dark { background: linear-gradient(150deg, var(--green) 0%, var(--green-dark) 100%); }
  .card .person { position: absolute; left: 5px; top: 17px; font-size: 4.4px; font-weight: 700; color: var(--green); }
  .card .role { position: absolute; left: 5px; top: 23px; font-size: 3.4px; color: var(--ink); }
  .card .contact { left: 5px; top: 30px; }
  .card .web { position: absolute; left: 0; right: 0; bottom: 9px; text-align: center; font-size: 3.6px; color: var(--paper); }
  .inside { position: absolute; width: 176px; height: 60px; background: var(--paper); box-shadow: 0 1px 4px rgba(0,0,0,.5); overflow: hidden; }
  .inside .photo { position: absolute; right: 0; top: 0; width: 78px; height: 100%; background: linear-gradient(120deg, #8c8f93, #4b5158 60%, #2f3439); }
  .inside .msg { position: absolute; left: 6px; top: 8px; width: 88px; font-size: 4.4px; line-height: 1.3; font-weight: 700; color: var(--green); }
  .inside .msg span { display: block; font-weight: 400; color: var(--ink); font-size: 3.6px; margin-top: 2px; }
</style>
</head>
<body>

<div class="label" style="left:30px;top:108px">C5 Envelope</div>
<div class="sheet envelope-c5" style="left:30px;top:120px;width:92px;height:56px">
  <div class="brand" style="left:6px;top:6px;font-size:4px"><span class="dot" style="width:5px;height:5px"></span>Cobalt Harvest</div>
  <svg class="swoosh bottom" viewBox="0 0 100 20" preserveAspectRatio="none" height="11"><path d="M0 20V12C40 4 70 18 100 6V20Z" fill="var(--green)"/></svg>
</div>
<div class="sheet envelope-c5-back" style="left:130px;top:128px;width:88px;height:48px;background:var(--paper-shade)">
  <svg class="swoosh top" viewBox="0 0 100 40" preserveAspectRatio="none" height="24"><path d="M0 0H100L50 38Z" fill="var(--paper)" stroke="var(--grey-line)" stroke-width=".6"/></svg>
</div>

<div class="label" style="left:30px;top:205px">DL Envelope</div>
<div class="sheet envelope-dl" style="left:30px;top:217px;width:66px;height:96px">
  <svg class="swoosh top" viewBox="0 0 100 40" preserveAspectRatio="none" height="20"><path d="M0 0H100V22C65 8 30 36 0 20Z" fill="var(--green)"/><path d="M0 26C30 40 65 14 100 28" stroke="var(--grey-line)" fill="none" stroke-width="1.2"/></svg>
  <div class="brand" style="left:6px;top:70px;font-size:4px"><span class="dot" style="width:5px;height:5px"></span>Cobalt Harvest</div>
</div>
<div class="sheet envelope-dl-front" style="left:106px;top:228px;width:112px;height:64px">
  <div class="brand" style="left:6px;top:6px;font-size:4px"><span class="dot" style="width:5px;height:5px"></span>Cobalt Harvest</div>
  <div class="lines" style="left:52px;top:30px;width:46px"><i></i><i></i><i></i></div>
  <svg class="swoosh bottom" viewBox="0 0 100 20" preserveAspectRatio="none" height="10"><path d="M0 20V10C40 2 70 18 100 6V20Z" fill="var(--green)"/></svg>
</div>

<div class="label" style="left:30px;top:328px">Compliments Slip</div>
<div class="sheet compliments" style="left:30px;top:340px;width:96px;height:56px">
  <div class="brand" style="left:6px;top:7px;font-size:4px"><span class="dot" style="width:5px;height:5px"></span>Cobalt Harvest</div>
  <div class="small-text" style="left:6px;top:22px;font-size:5px;font-weight:700;color:var(--green)">With Compliments</div>
  <svg class="swoosh bottom" viewBox="0 0 100 20" preserveAspectRatio="none" height="10"><path d="M0 20V10C40 2 70 18 100 6V20Z" fill="var(--green)"/></svg>
</div>
<div class="sheet compliments-small" style="left:134px;top:346px;width:84px;height:48px">
  <svg class="swoosh top" viewBox="0 0 100 20" preserveAspectRatio="none" height="9"><path d="M0 0H100V10C60 2 30 18 0 8Z" fill="var(--green)"/></svg>
  <div class="small-text" style="left:6px;top:16px">14 Brindle Lane Oakhurst Trading Park<br>Fenwick Cross Herts HP9 3QL</div>
  <div class="small-text" style="left:6px;top:32px;color:var(--green)">www.cobaltharvest-example.com</div>
</div>

<div class="label" style="left:272px;top:24px">A4 Invoice</div>
<div class="sheet invoice" style="left:272px;top:36px;width:180px;height:252px">
  <svg class="swoosh top" viewBox="0 0 100 30" preserveAspectRatio="none" height="40"><path d="M0 0H100V18C70 6 35 26 0 14Z" fill="var(--green)"/><path d="M0 20C35 32 70 12 100 22" stroke="var(--grey-line)" fill="none" stroke-width="1"/></svg>
  <div class="brand on-dark" style="left:12px;top:8px;font-size:6px"><span class="dot" style="width:7px;height:7px"></span>Cobalt Harvest</div>
  <div class="small-text" style="left:12px;top:50px">14 Brindle Lane Oakhurst Trading Park<br>Fenwick Cross Herts HP9 3QL</div>
  <div class="invoice-title">INVOICE</div>
  <table class="invoice-table">
    <thead><tr><th>Item</th><th>Description</th><th>Qty</th><th>Price</th><th>Total</th></tr></thead>
    <tbody>
      <tr><td>01</td><td>Equipment collection</td><td>1</td><td>0.00</td><td>0.00</td></tr>
      <tr><td>02</td><td>Data wiping service</td><td>1</td><td>0.00</td><td>0.00</td></tr>
      <tr><td>03</td><td>Recycling report</td><td>1</td><td>0.00</td><td>0.00</td></tr>
      <tr><td></td><td></td><td></td><td>Total</td><td>0.00</td></tr>
    </tbody>
  </table>
  <svg class="swoosh bottom" viewBox="0 0 100 20" preserveAspectRatio="none" height="14"><path d="M0 20V12C40 2 70 18 100 8V20Z" fill="var(--green)"/></svg>
</div>

<div class="label" style="left:470px;top:24px">A4 Letterhead</div>
<div class="sheet letterhead" style="left:470px;top:36px;width:176px;height:252px">
  <svg class="swoosh top" viewBox="0 0 100 30" preserveAspectRatio="none" height="40"><path d="M0 0H100V18C70 6 35 26 0 14Z" fill="var(--green)"/><path d="M0 20C35 32 70 12 100 22" stroke="var(--grey-line)" fill="none" stroke-width="1"/></svg>
  <div class="brand on-dark" style="left:12px;top:8px;font-size:6px"><span class="dot" style="width:7px;height:7px"></span>Cobalt Harvest</div>
  <div class="small-text" style="left:12px;top:226px">14 Brindle Lane Oakhurst Trading Park Fenwick Cross Herts HP9 3QL<br>www.cobaltharvest-example.com</div>
  <svg class="swoosh bottom" viewBox="0 0 100 20" preserveAspectRatio="none" height="14"><path d="M0 20V12C40 2 70 18 100 8V20Z" fill="var(--green)"/></svg>
</div>

<div class="label" style="left:662px;top:24px">A4 Letterhead continued</div>
<div class="sheet letterhead-continued" style="left:662px;top:36px;width:178px;height:252px">
  <svg class="swoosh top" viewBox="0 0 100 30" preserveAspectRatio="none" height="22"><path d="M0 0H100V14C70 4 35 22 0 10Z" fill="var(--green)"/></svg>
  <svg class="swoosh bottom" viewBox="0 0 100 20" preserveAspectRatio="none" height="10"><path d="M0 20V12C40 2 70 18 100 8V20Z" fill="var(--green)"/></svg>
</div>

<div class="label" style="left:860px;top:18px">Presentation Folder</div>
<div class="item folder" style="left:860px;top:30px;width:320px;height:262px">
  <div class="folder-panel folder-inside" style="left:0;width:160px">
    <svg class="pocket" viewBox="0 0 100 60" preserveAspectRatio="none"><path d="M0 10C40 0 70 14 100 4V60H0Z" fill="var(--paper-shade)"/><path d="M0 50C40 40 70 58 100 46V60H0Z" fill="var(--green)"/></svg>
    <div class="card-slot"></div>
  </div>
  <div class="folder-panel folder-front" style="left:162px;width:158px">
    <div class="ring"></div>
    <div class="brand on-dark" style="left:50%;top:62%;transform:translateX(-50%);font-size:6px"><span class="dot" style="width:7px;height:7px"></span>Cobalt Harvest</div>
    <svg class="swoosh bottom" viewBox="0 0 100 30" preserveAspectRatio="none" height="40"><path d="M0 30V18C35 6 65 26 100 12V30Z" fill="var(--paper)"/></svg>
  </div>
</div>

<div class="label" style="left:272px;top:338px">Business Card – Director</div>
<div class="card front" style="left:272px;top:350px">
  <svg class="swoosh top" viewBox="0 0 100 20" preserveAspectRatio="none" height="12"><path d="M0 0H100V10C60 2 30 18 0 8Z" fill="var(--green)"/></svg>
  <div class="person">Director Name</div><div class="role">Director</div>
  <div class="small-text contact">info@cobaltharvest-example.com<br>14 Brindle Lane, Fenwick Cross</div>
</div>
<div class="card dark back" style="left:362px;top:350px">
  <div class="brand on-dark" style="left:50%;top:16px;transform:translateX(-50%);font-size:5px"><span class="dot" style="width:6px;height:6px"></span>Cobalt Harvest</div>
  <div class="web">www.cobaltharvest-example.com</div>
</div>

<div class="label" style="left:454px;top:338px">Business Card – Director</div>
<div class="card front" style="left:454px;top:350px">
  <svg class="swoosh top" viewBox="0 0 100 20" preserveAspectRatio="none" height="12"><path d="M0 0H100V10C60 2 30 18 0 8Z" fill="var(--green)"/></svg>
  <div class="person">Director Name</div><div class="role">Director</div>
  <div class="small-text contact">www.cobaltharvest-example.com<br>14 Brindle Lane, Fenwick Cross</div>
</div>
<div class="card dark back" style="left:544px;top:350px">
  <div class="brand on-dark" style="left:50%;top:16px;transform:translateX(-50%);font-size:5px"><span class="dot" style="width:6px;height:6px"></span>Cobalt Harvest</div>
  <div class="web">www.cobaltharvest-example.com</div>
</div>

<div class="label" style="left:636px;top:338px">Folded Card – Director</div>
<div class="card front" style="left:636px;top:350px">
  <svg class="swoosh bottom" viewBox="0 0 100 20" preserveAspectRatio="none" height="12"><path d="M0 20V10C40 2 70 18 100 6V20Z" fill="var(--green)"/></svg>
  <div class="brand" style="left:5px;top:5px;font-size:4px"><span class="dot" style="width:5px;height:5px"></span>Cobalt Harvest</div>
  <div class="person">Director Name</div><div class="role">Director</div>
</div>
<div class="card dark back" style="left:726px;top:350px">
  <div class="brand on-dark" style="left:50%;top:16px;transform:translateX(-50%);font-size:5px"><span class="dot" style="width:6px;height:6px"></span>Cobalt Harvest</div>
  <div class="web">www.cobaltharvest-example.com</div>
</div>

<div class="label" style="left:818px;top:338px">Folded Card – Director</div>
<div class="card front" style="left:818px;top:350px">
  <svg class="swoosh bottom" viewBox="0 0 100 20" preserveAspectRatio="none" height="12"><path d="M0 20V10C40 2 70 18 100 6V20Z" fill="var(--green)"/></svg>
  <div class="brand" style="left:5px;top:5px;font-size:4px"><span class="dot" style="width:5px;height:5px"></span>Cobalt Harvest</div>
  <div class="person">Director Name</div><div class="role">Director</div>
</div>
<div class="card dark back" style="left:908px;top:350px">
  <div class="brand on-dark" style="left:50%;top:16px;transform:translateX(-50%);font-size:5px"><span class="dot" style="width:6px;height:6px"></span>Cobalt Harvest</div>
  <div class="web">www.cobaltharvest-example.com</div>
</div>

<div class="label" style="left:1000px;top:338px">Folded Card – Company</div>
<div class="card front" style="left:1000px;top:350px">
  <svg class="swoosh bottom" viewBox="0 0 100 20" preserveAspectRatio="none" height="12"><path d="M0 20V10C40 2 70 18 100 6V20Z" fill="var(--green)"/></svg>
  <div class="brand" style="left:5px;top:12px;font-size:5px"><span class="dot" style="width:6px;height:6px"></span>Cobalt Harvest</div>
  <div class="small-text" style="left:5px;top:24px">14 Brindle Lane Oakhurst Trading Park<br>Fenwick Cross Herts HP9 3QL</div>
</div>
<div class="card dark back" style="left:1090px;top:350px">
  <div class="brand on-dark" style="left:50%;top:16px;transform:translateX(-50%);font-size:5px"><span class="dot" style="width:6px;height:6px"></span>Cobalt Harvest</div>
  <div class="web">www.cobaltharvest-example.com</div>
</div>

<div class="inside" style="left:272px;top:408px">
  <div class="msg">Redundant IT &amp; Computer Equipment<span>Corporate business people wanted</span></div>
  <div class="photo" role="img" aria-label="Photo of business people"></div>
</div>
<div class="inside" style="left:454px;top:408px">
  <div class="msg">Redundant IT &amp; Computer Equipment<span>All UK areas covered</span></div>
  <div class="photo" role="img" aria-label="Photo of business people"></div>
</div>
<div class="inside" style="left:636px;top:408px">
  <div class="msg">Redundant IT &amp; Computer Equipment<span>Corporate business people wanted</span></div>
  <div class="photo" role="img" aria-label="Photo of business people"></div>
</div>
<div class="inside" style="left:818px;top:408px">
  <div class="msg">Redundant IT &amp; Computer Equipment<span>All UK areas covered</span></div>
  <div class="photo" role="img" aria-label="Photo of business people"></div>
</div>
<div class="inside" style="left:1000px;top:408px">
  <div class="msg">Redundant IT &amp; Computer Equipment<span>Corporate business people wanted</span></div>
  <div class="photo" role="img" aria-label="Photo of business people"></div>
</div>

</body>
</html>
```